Dravetti Business Cards

We need a business card design for Dravetti Mining.

This is a B2B company that buys and sells large machinery tires within the coal mining industry. The design should the strong, crisp and masculine. I have uploaded the company logo and rough mock-up of what the back of the card should look like. the front of the card should have the same look/feel as the back. I need editable templates for both the front and the back of the card.

Color scheme should be grey/green/black

Contact information to include on the card:
Name: Owen Pellsworth
Title: Managing Director
Phone: 972-555-0143
Address: 3157 Brantley #5 Dallas, TX 75209
Email: Owen@Dravetti-example.com

I am also opening a contest for letterhead design. If you submit a business card design, please also submit a letterhead design with the same look/feel. The winner of the business card design will also will the letter head and be paid for both.

Target Market(s)

Procurement men/women in the coal mining industry

Industry/Entity Type

Coal Mining

```html
<!DOCTYPE html>
<html lang="en">
<head>
<meta charset="utf-8">
<title>Dravetti Mining – Business Cards</title>
<link rel="stylesheet" href="https://fonts.googleapis.com/css2?family=Michroma&display=swap">
<style>
  :root {
    --bg: #2b2b2d;
    --card-dark: #1c1c1f;
    --card-mid: #26262a;
    --green: #4fa317;
    --green-deep: #3f8a10;
    --white: #f2f2f2;
    --grey: #cfcfd2;
  }
  * { margin: 0; padding: 0; box-sizing: border-box; }
  html, body {
    width: 1200px; height: 900px; overflow: hidden;
    background: var(--bg);
    font-family: "Michroma", sans-serif;
  }
  .sheet {
    width: 1200px; height: 900px;
    display: flex; flex-direction: column;
    align-items: center; justify-content: center; gap: 48px;
  }
  .card {
    position: relative;
    width: 700px; height: 400px;
    background: linear-gradient(160deg, var(--card-mid), var(--card-dark));
    box-shadow: 0 10px 30px rgba(0,0,0,.45);
    overflow: hidden;
  }
  /* Back */
  .card-back { display: flex; align-items: center; justify-content: center; }
  .back-brand { display: flex; align-items: center; gap: 22px; }
  .brand-square { width: 34px; height: 34px; background: var(--green); }
  .back-name { color: var(--white); font-size: 46px; letter-spacing: 2px; }
  /* Front */
  .front-brand {
    position: absolute; left: 60px; top: 62px;
    display: flex; align-items: center; gap: 16px;
  }
  .front-brand .brand-square { width: 26px; height: 26px; }
  .brand-words { display: flex; flex-direction: column; }
  .brand-name { color: var(--white); font-size: 34px; letter-spacing: 1px; line-height: 1; }
  .brand-sector {
    color: var(--green); font-size: 11px; letter-spacing: 22px;
    margin-top: 6px; padding-left: 4px;
  }
  .contact {
    position: absolute; left: 150px; top: 176px;
    font-variant: small-caps; letter-spacing: 1.5px;
  }
  .person-name { color: var(--green); font-size: 20px; }
  .person-title { color: var(--white); font-size: 12px; margin-top: 4px; }
  .lines { margin-top: 22px; font-size: 13px; line-height: 1.6; }
  .lines dt { color: var(--green); display: inline-block; width: 82px; }
  .lines dd { color: var(--white); display: inline; }
  .lines div { display: block; }
  .address { color: var(--grey); font-size: 14px; margin-top: 20px; }
  .green-band {
    position: absolute; left: 0; right: 0; bottom: 10px; height: 34px;
    background: linear-gradient(180deg, var(--green), var(--green-deep));
  }
</style>
</head>
<body>
  <main class="sheet">
    <section class="card card-back" aria-label="Card back">
      <div class="back-brand">
        <span class="brand-square"></span>
        <span class="back-name">DRAVETTI</span>
      </div>
    </section>

    <section class="card card-front" aria-label="Card front">
      <div class="front-brand">
        <span class="brand-square"></span>
        <div class="brand-words">
          <span class="brand-name">DRAVETTI</span>
          <span class="brand-sector">MINING</span>
        </div>
      </div>

      <div class="contact">
        <p class="person-name">Owen Pellsworth</p>
        <p class="person-title">Managing Director</p>
        <dl class="lines">
          <div><dt>Phone:</dt><dd>972-555-0143</dd></div>
          <div><dt>Email:</dt><dd>Owen@Dravetti-example.com</dd></div>
        </dl>
        <p class="address">3157 Brantley #5 Dallas, TX 75209</p>
      </div>

      <div class="green-band"></div>
    </section>
  </main>
</body>
</html>
```